New Business Card for General Contractor Marketing

Need a business card the is more like a marketing promotion of our services
Must be horizontal orientation, One Sided Only, Max font size, Organize the Services
#1 General Contractor for Realtors
Remodels – Renovations – Repairs
Water & Mold Damage Experts
Painting: Interior/ Exterior
Flooring: Wood / LVT / Carpet
Plumbing: Repairs & Upgrades
Electric: Lights & Energy Efficient Upgrades
Kitchen & Bath Remodels
Fast Inspections Repair Billed Thru Escrow
BrightHarborBuilds.com
555-418-2796

Industry/Entity Type

General Contractor

Contact Information for Business Card

One Sided Only: #1 General Contractor for Realtors Remodels – Renovations – Repairs Water & Mold Damage Experts Painting: Interior/ Exterior Flooring: Wood / LVT / Carpet Plumbing: Repairs & Upgrades Electric: Lights & Energy Efficient Upgrades Kitchen & Bath Remodels Fast Inspections Repair Billed Thru Escrow BrightHarborBuilds.com 555-418-2796

Colors
0054AA
0677BA
7BADD7
CADEEF
E8F1F8

Requirements
Must have
• One Sided Only: #1 General Contractor for Realtors Remodels – Renovations – Repairs Water & Mold Damage Experts Painting: Interior/ Exterior Flooring: Wood / LVT / Carpet Plumbing: Repairs & Upgrades Electric: Lights & Energy Efficient Upgrades Kitchen & Bath Remodels Fast Inspections Repair Billed Thru Escrow BrightHarborBuilds.com 555-418-2796

```html
<!DOCTYPE html>
<html lang="en">
<head>
<meta charset="utf-8">
<title>BrightHarborBuilds Business Card</title>
<link href="https://fonts.googleapis.com/css2?family=Montserrat:ital,wght@0,600;0,700;0,800;0,900;1,600&display=swap" rel="stylesheet">
<style>
  :root {
    --orange: #f47f20;
    --navy: #1b2a52;
    --panel: #172a55;
    --panel-deep: #0f1f44;
    --white: #ffffff;
    --page: #eef1f4;
  }
  * { box-sizing: border-box; margin: 0; padding: 0; }
  html, body {
    width: 1200px; height: 960px; overflow: hidden;
    background: var(--page);
    font-family: "Montserrat", Arial, sans-serif;
  }
  .card {
    position: absolute; left: 100px; top: 188px;
    width: 1000px; height: 584px;
    background: var(--white);
    box-shadow: 0 6px 24px rgba(20, 30, 60, 0.12);
    overflow: hidden;
  }
  /* Left side */
  .brand-side { position: absolute; left: 0; top: 0; width: 446px; height: 100%; }
  .rank-band {
    position: absolute; left: 0; top: 0; width: 100%; height: 66px;
    background: var(--orange);
  }
  .rank-badge {
    position: absolute; left: 18px; top: 12px;
    width: 76px; height: 76px; border-radius: 50%;
    background: var(--navy); border: 3px solid var(--white);
    color: var(--white); font-weight: 900; font-size: 38px;
    display: flex; align-items: center; justify-content: center;
    letter-spacing: -1px;
  }
  .rank-text {
    position: absolute; left: 116px; top: 13px;
    color: var(--navy); font-weight: 800; font-size: 19px; line-height: 21px;
    letter-spacing: 0.3px;
  }
  .brand-name {
    position: absolute; left: 0; top: 296px; width: 100%;
    text-align: center; color: var(--navy);
    font-weight: 800; font-size: 26px; letter-spacing: -0.5px;
  }
  .brand-tagline {
    position: absolute; left: 0; top: 332px; width: 100%;
    text-align: center; color: var(--navy);
    font-weight: 800; font-size: 20px; letter-spacing: 0.4px;
  }
  .offer-list {
    position: absolute; left: 76px; top: 398px; list-style: none;
  }
  .offer-list li {
    display: flex; align-items: center; gap: 14px;
    height: 45px;
    color: var(--navy); font-weight: 800; font-size: 26px; letter-spacing: 0.5px;
  }
  .offer-list svg { width: 26px; height: 26px; flex: none; }

  /* Right side */
  .services-side {
    position: absolute; left: 446px; top: 0; width: 554px; height: 100%;
    background: var(--panel);
  }
  .skyline {
    position: absolute; left: 0; top: 330px; width: 100%; height: 168px;
    background: linear-gradient(180deg, rgba(15,31,68,0) 0%, var(--panel-deep) 100%);
  }
  .service {
    position: absolute; left: 0; width: 100%; text-align: center;
  }
  .service-title {
    color: var(--orange); font-weight: 800; font-size: 26px; line-height: 30px;
    letter-spacing: 0.5px;
  }
  .service-detail {
    color: var(--white); font-weight: 800; font-size: 27px; line-height: 32px;
    letter-spacing: 0.5px;
  }
  .service-note {
    color: var(--white); font-weight: 800; font-size: 14px; line-height: 18px;
    letter-spacing: 0.3px;
  }
  .escrow-note {
    position: absolute; left: 0; top: 474px; width: 100%; text-align: center;
    color: var(--white); font-style: italic; font-weight: 600; font-size: 16px;
    letter-spacing: 0.2px;
  }
  .phone-band {
    position: absolute; left: 0; bottom: 0; width: 100%; height: 87px;
    background: var(--orange);
    display: flex; align-items: center; justify-content: center; gap: 22px;
  }
  .phone-icon {
    width: 44px; height: 44px; border-radius: 8px; background: var(--navy);
    display: flex; align-items: center; justify-content: center;
  }
  .phone-number {
    color: var(--white); font-weight: 800; font-size: 56px; letter-spacing: 0.5px;
  }
</style>
</head>
<body>
  <div class="card">
    <section class="brand-side">
      <div class="rank-band"></div>
      <div class="rank-badge">#1</div>
      <p class="rank-text">GENERAL CONTRACTOR<br>FOR REALTORS</p>

      <p class="brand-name">BRIGHTHARBORBUILDS.COM</p>
      <p class="brand-tagline">WATER &amp; MOLD DAMAGE EXPERTS</p>

      <ul class="offer-list">
        <li><svg viewBox="0 0 26 26"><circle cx="13" cy="13" r="12" fill="#f47f20"/><path d="M7 13.5l4 4 8-8.5" fill="none" stroke="#fff" stroke-width="3" stroke-linecap="round" stroke-linejoin="round"/></svg>REMODELS</li>
        <li><svg viewBox="0 0 26 26"><circle cx="13" cy="13" r="12" fill="#f47f20"/><path d="M7 13.5l4 4 8-8.5" fill="none" stroke="#fff" stroke-width="3" stroke-linecap="round" stroke-linejoin="round"/></svg>RENOVATIONS</li>
        <li><svg viewBox="0 0 26 26"><circle cx="13" cy="13" r="12" fill="#f47f20"/><path d="M7 13.5l4 4 8-8.5" fill="none" stroke="#fff" stroke-width="3" stroke-linecap="round" stroke-linejoin="round"/></svg>REPAIRS</li>
      </ul>
    </section>

    <section class="services-side">
      <div class="skyline" role="img" aria-label="Faint silhouette of house rooftops"></div>

      <div class="service" style="top:38px">
        <p class="service-title">PAINTING</p>
        <p class="service-detail">INTERIOR/ EXTERIOR</p>
      </div>
      <div class="service" style="top:136px">
        <p class="service-title">FLOORING</p>
        <p class="service-detail">WOOD / LVT / CARPET</p>
      </div>
      <div class="service" style="top:244px">
        <p class="service-title">PLUMBING</p>
        <p class="service-detail">REPAIRS &amp; UPGRADES</p>
      </div>
      <div class="service" style="top:341px">
        <p class="service-title">ELECTRIC</p>
        <p class="service-detail">LIGHTS &amp; ENERGY</p>
        <p class="service-note">EFFICIENT UPGRADES KITCHEN &amp; BATH REMODELS</p>
      </div>

      <p class="escrow-note">FAST INSPECTIONS REPAIR BILLED THRU ESCROW</p>

      <div class="phone-band">
        <div class="phone-icon">
          <svg width="28" height="28" viewBox="0 0 24 24"><path d="M6.6 10.8a15.1 15.1 0 0 0 6.6 6.6l2.2-2.2a1 1 0 0 1 1-.25 11.4 11.4 0 0 0 3.6.57 1 1 0 0 1 1 1V20a1 1 0 0 1-1 1A17 17 0 0 1 3 4a1 1 0 0 1 1-1h3.5a1 1 0 0 1 1 1c0 1.25.2 2.45.57 3.57a1 1 0 0 1-.25 1z" fill="#f47f20"/></svg>
        </div>
        <p class="phone-number">555-418-2796</p>
      </div>
    </section>
  </div>
</body>
</html>
```